Social Media Card

We would like a social media card to hand out to our customers.
It should be double sided, with the front to say in bold letters Follow Us!
We would like the card to be two toned in our brand colors (espresso brown & copper.) I still want a modern, clean look to the card but it can be a bit more "fun" than our business cards. I have attached the previous card that you did but you don't have to stick to the brown background/copper lettering as shown.
The font is josefin. We would need our logo either on the front or the back side.
I think I want social media icons but not the same old boring ones.
Our social media information is as follows:
Facebook: Valmonte Jewelry
Twitter: Valmonte Jewelry
Pinterest: vmkqpw
Instagram: Valmonte Jewelry
Looking forward to seeing what you come up with!
Thanks!
Gwen

Our address, etc info will need to be added.

Brisbury Lane # 7

Stonegate Plaza

Harwick Falls, VT 03053

(603)519-8074

www.valmontejewelry.example

info@valmontejewelry.example

```html
<!DOCTYPE html>
<html lang="en">
<head>
<meta charset="utf-8">
<title>Valmonte Jewelry – Card Set</title>
<link rel="stylesheet" href="https://fonts.googleapis.com/css2?family=Josefin+Sans:wght@300;400&display=swap">
<style>
  :root {
    --espresso: #2a1810;
    --copper: #c4692a;
    --copper-deep: #7b3d17;
    --copper-pale: #f3d6bf;
    --paper: #ffffff;
    --ink: #1c1c1c;
    --ink-soft: #6d6d6d;
    --stage: #e4e4e8;
  }
  * { box-sizing: border-box; margin: 0; padding: 0; }
  html, body {
    width: 1200px; height: 900px; overflow: hidden;
    background: var(--stage);
    font-family: "Josefin Sans", sans-serif;
  }
  .card-set {
    position: absolute; left: 150px; top: 50px;
    display: grid;
    grid-template-columns: repeat(2, 420px);
    grid-auto-rows: 240px;
    gap: 40px 60px;
  }
  .card {
    position: relative; overflow: hidden;
    box-shadow: 0 3px 10px rgba(0,0,0,.22);
  }
  .card--dark { background: var(--espresso); color: var(--copper); }
  .card--light { background: var(--paper); color: var(--ink); }

  /* Name block: one colour, one weight, one plain circle */
  .brand-name {
    position: absolute; left: 0; right: 0;
    display: flex; align-items: center; justify-content: center; gap: 12px;
    font-weight: 400; line-height: 1; white-space: nowrap;
  }
  .brand-name__dot {
    flex: none; border-radius: 50%; background: currentColor;
  }

  .brand-front .brand-name { top: 104px; font-size: 36px; }
  .brand-front .brand-name__dot { width: 14px; height: 14px; }

  .brand-light .brand-name { top: 40px; font-size: 24px; color: var(--ink); }
  .brand-light .brand-name__dot { width: 10px; height: 10px; }

  .social .brand-name { top: 82px; font-size: 24px; }
  .social .brand-name__dot { width: 10px; height: 10px; }

  /* Business card back */
  .contact .product-photo {
    position: absolute; right: 0; top: 0; width: 170px; height: 130px;
    background: radial-gradient(circle at 55% 55%, #cfd2cf 0 22%, #eef0ee 45%, #ffffff 75%);
  }
  .contact__name {
    position: absolute; left: 34px; top: 118px;
    font-size: 26px; font-weight: 400; color: var(--ink);
  }
  .contact__details {
    position: absolute; left: 34px; top: 156px;
    list-style: none; font-size: 10.5px; font-weight: 300;
    line-height: 1.45; color: var(--ink-soft);
  }

  /* Headline cards */
  .headline {
    position: absolute; inset: 0;
    display: flex; align-items: center; justify-content: center;
    font-weight: 400; text-transform: uppercase; color: var(--copper);
    white-space: nowrap;
  }
  .want .headline { font-size: 80px; letter-spacing: .14em; padding-left: .14em; }
  .follow .headline { font-size: 50px; letter-spacing: .05em; }

  /* Social back */
  .social__band {
    position: absolute; left: 0; right: 0; top: 0; height: 44px;
    background: var(--copper-deep);
  }
  .social__url {
    position: absolute; left: 26px; right: 16px; top: 8px; height: 28px;
    border-radius: 14px; background: var(--copper);
    color: var(--copper-pale); font-size: 15px; font-weight: 300;
    padding: 7px 0 0 22px;
  }
  .social__list {
    position: absolute; left: 18px; right: 12px; bottom: 28px;
    display: flex; justify-content: space-between; list-style: none;
  }
  .social__item {
    display: flex; align-items: center; gap: 6px;
    font-size: 9.5px; font-weight: 300; color: var(--copper);
    white-space: nowrap;
  }
  .social__dot { flex: none; width: 22px; height: 22px; border-radius: 50%; background: var(--copper-deep); }
</style>
</head>
<body>
<main class="card-set">

  <section class="card card--dark brand-front">
    <div class="brand-name"><span class="brand-name__dot"></span>Valmonte Jewelry</div>
  </section>

  <section class="card card--light contact">
    <div class="product-photo" role="img" aria-label="Product photo: silver wire pendant with a green gemstone on a fine chain"></div>
    <h2 class="contact__name">Gwen Valmonte</h2>
    <ul class="contact__details">
      <li>Brisbury Lane # 7 · Stonegate Plaza</li>
      <li>Harwick Falls, VT 05391</li>
      <li>(802)519-8074</li>
      <li>info@valmontejewelry.example</li>
      <li>www.valmontejewelry.example</li>
    </ul>
  </section>

  <section class="card card--light brand-light">
    <div class="brand-name"><span class="brand-name__dot"></span>Valmonte Jewelry</div>
  </section>

  <section class="card card--dark want">
    <p class="headline">Want !</p>
  </section>

  <section class="card card--dark follow">
    <p class="headline">Follow Us</p>
  </section>

  <section class="card card--dark social">
    <div class="social__band"></div>
    <div class="social__url">valmontejewelry.example</div>
    <div class="brand-name"><span class="brand-name__dot"></span>Valmonte Jewelry</div>
    <ul class="social__list">
      <li class="social__item"><span class="social__dot"></span>Valmonte Jewelry</li>
      <li class="social__item"><span class="social__dot"></span>Valmonte Jewelry</li>
      <li class="social__item"><span class="social__dot"></span>vmkqpw</li>
      <li class="social__item"><span class="social__dot"></span>Valmonte Jewelry</li>
    </ul>
  </section>

</main>
</body>
</html>
```